Norwell Asset Partners, LLC

I need a new business card desperately.

Please update my business card. I am looking for a professional modern classy design like the Brisket Holdings card in the attachments.

Industry/Entity Type

Investment

Contact Information for Business Card

Colors

Designer to choose colors to be used in the design.

```html
<!DOCTYPE html>
<html lang="en">
<head>
<meta charset="utf-8">
<title>Norwell Asset Partners, LLC — Business Card</title>
<link href="https://fonts.googleapis.com/css2?family=Open+Sans:wght@400;600;700&display=swap" rel="stylesheet">
<style>
  :root {
    --slate: #59636f;
    --card: #ffffff;
    --backdrop: #d8dadd;
    --rule: #ffffff;
  }
  html, body {
    margin: 0;
    padding: 0;
    width: 1200px;
    height: 675px;
    overflow: hidden;
    background: var(--backdrop);
  }
  .canvas {
    position: relative;
    width: 1200px;
    height: 675px;
  }
  .business-card {
    position: absolute;
    left: 180px;
    top: 97px;
    width: 840px;
    height: 480px;
    background: var(--card);
    overflow: hidden;
    font-family: "Open Sans", sans-serif;
    color: var(--slate);
    box-shadow: 0 6px 20px rgba(0,0,0,0.12);
  }
  .brand {
    position: absolute;
    left: 150px;
    top: 92px;
    display: flex;
    align-items: center;
    gap: 26px;
  }
  .brand-square {
    width: 64px;
    height: 64px;
    background: var(--slate);
  }
  .brand-name {
    font-size: 30px;
    font-weight: 600;
    letter-spacing: 1.5px;
    text-transform: uppercase;
    line-height: 1;
  }
  .person {
    position: absolute;
    left: 118px;
    top: 238px;
    text-align: right;
  }
  .person-name {
    font-size: 34px;
    font-weight: 700;
    line-height: 1.1;
  }
  .person-title {
    font-size: 18px;
    font-weight: 600;
    margin-top: 2px;
  }
  .contact {
    position: absolute;
    left: 430px;
    top: 240px;
    font-size: 21px;
    font-weight: 600;
    line-height: 1.45;
  }
  .contact p { margin: 0; }
  .footer-band {
    position: absolute;
    left: 0;
    bottom: 0;
    width: 840px;
    height: 86px;
  }
</style>
</head>
<body>
<main class="canvas">
  <section class="business-card" aria-label="Business card front">
    <div class="brand">
      <div class="brand-square"></div>
      <div class="brand-name">Norwell Asset Partners, LLC</div>
    </div>

    <div class="person">
      <div class="person-name">Grant L, Mercer</div>
      <div class="person-title">Managing Partner</div>
    </div>

    <div class="contact">
      <p>2874 Marlow Creek Lane</p>
      <p>Round Rock, Tx 78681</p>
      <p>Direct: 512.55.0142</p>
      <p>Gmercer@norwellasset.com</p>
    </div>

    <svg class="footer-band" viewBox="0 0 840 86" aria-hidden="true">
      <rect x="0" y="0" width="840" height="86" fill="var(--slate)"/>
      <line x1="500" y1="86" x2="548" y2="52" stroke="var(--rule)" stroke-width="4"/>
    </svg>
  </section>
</main>
</body>
</html>
```